Velno Recycling needs a new web design

We need a new web design for our company based in Austin, TX. We resell and recycling electronics such as laptops, computer components, Tovlets, Brunos, etc. Since our inception over ten years ago, we’ve become one of the premier electronics recycling and remarketing companies in Austin, Texas.

```html
<!DOCTYPE html>
<html lang="en">
<head>
<meta charset="utf-8">
<title>Velno Recycling – Computer Recycling Made Easy</title>
<link rel="stylesheet" href="https://fonts.googleapis.com/css2?family=Montserrat:wght@300;400;600;700&family=Roboto:wght@300;400;500&display=swap">
<style>
  :root {
    --blue: #0b5fb0;
    --blue-bright: #1273c4;
    --blue-dark: #0a4f99;
    --orange: #ff9500;
    --hero-bg: #eaf6f5;
    --services-bg: #f8f8f8;
    --ink: #111;
    --text: #4a4a4a;
    --white: #fff;
  }
  * { box-sizing: border-box; margin: 0; padding: 0; }
  html, body { width: 722px; height: 1200px; overflow: hidden; }
  body { position: relative; background: var(--white); font-family: "Roboto", Arial, sans-serif; color: var(--text); }
  .abs { position: absolute; }

  /* Header */
  .site-header { position: absolute; left: 0; top: 0; width: 722px; height: 40px; background: var(--white); }
  .brand { position: absolute; left: 104px; top: 9px; display: flex; align-items: center; gap: 5px; }
  .brand-mark { width: 20px; height: 20px; border-radius: 50%; background: var(--blue); }
  .brand-name { font-family: "Montserrat", Arial, sans-serif; font-weight: 700; font-size: 13px; color: var(--blue); letter-spacing: .2px; }
  .main-nav { position: absolute; left: 472px; top: 0; display: flex; height: 40px; }
  .main-nav a { display: block; height: 40px; line-height: 40px; font-family: "Montserrat", Arial, sans-serif; font-weight: 600; font-size: 7.5px; color: var(--ink); text-decoration: none; padding: 0 6px; margin-right: 4px; }
  .main-nav a.is-active { background: var(--blue-bright); color: var(--white); padding: 0 6px; }

  /* Hero */
  .hero { position: absolute; left: 0; top: 40px; width: 722px; height: 297px; background: var(--hero-bg); }
  .hero-kicker { position: absolute; left: 105px; top: 80px; font-family: "Montserrat", Arial, sans-serif; font-weight: 400; font-size: 20.5px; color: var(--blue-bright); letter-spacing: .3px; }
  .hero-title { position: absolute; left: 104px; top: 96px; font-family: "Montserrat", Arial, sans-serif; font-weight: 700; font-size: 39px; line-height: 1; color: var(--ink); letter-spacing: .5px; }
  .hero-title span { color: var(--blue-bright); }
  .hero-copy { position: absolute; left: 106px; top: 141px; width: 240px; font-size: 6.3px; line-height: 9.6px; color: #333; }
  .btn { position: absolute; display: block; border-radius: 12px; background: var(--orange); color: var(--white); font-family: "Montserrat", Arial, sans-serif; font-weight: 600; font-size: 7.5px; text-align: center; text-decoration: none; }
  .hero .btn { left: 105px; top: 200px; width: 99px; height: 22px; line-height: 22px; }
  .hero-media { position: absolute; left: 365px; top: 20px; width: 250px; height: 255px; border-radius: 6px; background: linear-gradient(180deg, #d8d2c4 0%, #bfb9ad 38%, #1f4fb8 40%, #1a3f9c 100%); }

  /* About */
  .about { position: absolute; left: 0; top: 337px; width: 722px; height: 285px; background: var(--white); }
  .about-media { position: absolute; left: 110px; top: 10px; width: 220px; height: 240px; border-radius: 50% 50% 50% 50% / 46% 46% 54% 54%; background: radial-gradient(circle at 50% 60%, #f4f4f4 0 55%, #eef0f2 56%, #ffffff 100%); }
  .about-media::after { content: ""; position: absolute; left: 48px; top: 30px; width: 130px; height: 185px; border-radius: 10px; background: linear-gradient(180deg, #2a4f7c 0%, #4f7fc0 55%, #6cc42a 62%, #4ea51a 100%); opacity: .85; }
  .section-title { font-family: "Montserrat", Arial, sans-serif; font-weight: 700; color: var(--blue); letter-spacing: .5px; }
  .about .section-title { position: absolute; left: 359px; top: 68px; font-size: 25px; }
  .about-copy { position: absolute; left: 359px; top: 104px; width: 242px; font-size: 6.9px; line-height: 11.8px; color: var(--text); }
  .about .btn { left: 357px; top: 195px; width: 99px; height: 22px; line-height: 22px; }

  /* Services */
  .services { position: absolute; left: 0; top: 622px; width: 722px; height: 264px; background: var(--services-bg); }
  .services .section-title { position: absolute; left: 0; width: 722px; top: 19px; text-align: center; font-size: 25px; }
  .service { position: absolute; top: 78px; width: 230px; text-align: center; }
  .service--ewaste { left: 127px; }
  .service--pickup { left: 373px; }
  .service-icon { display: block; margin: 0 auto; height: 70px; }
  .service-name { margin-top: 9px; font-size: 13px; font-weight: 400; color: var(--blue); }
  .service-tag { margin-top: 1px; font-size: 8px; color: var(--ink); }
  .service-copy { margin-top: 6px; font-size: 6.8px; line-height: 10.2px; color: var(--text); }

  /* Contact */
  .contact { position: absolute; left: 0; top: 886px; width: 722px; height: 314px; background: var(--blue-bright); }
  .contact-backdrop { position: absolute; inset: 0; background: linear-gradient(100deg, #0e6bbd 0%, #1675c6 45%, #2a82cc 70%, #1370c2 100%); }
  .contact-title { position: absolute; left: 0; width: 722px; top: 17px; text-align: center; font-family: "Montserrat", Arial, sans-serif; font-weight: 600; font-size: 16.5px; letter-spacing: 1.2px; color: var(--white); }
  .contact-form { position: absolute; left: 205px; top: 51px; width: 312px; }
  .field { display: block; width: 312px; height: 27px; margin-bottom: 4px; background: var(--white); border: 0; border-radius: 2px; padding: 0 9px; font-family: "Roboto", Arial, sans-serif; font-size: 7px; color: #555; line-height: 27px; }
  .field--message { height: 62px; line-height: 1; padding-top: 10px; margin-top: 2px; }
  .btn-submit { display: block; width: 312px; height: 25px; margin-top: 9px; border-radius: 2px; background: var(--orange); color: var(--white); font-family: "Roboto", Arial, sans-serif; font-weight: 500; font-size: 7px; text-align: center; line-height: 25px; }
  .contact-details { position: absolute; left: 0; width: 722px; top: 257px; text-align: center; color: var(--white); font-size: 8.4px; font-weight: 500; }
  .copyright { position: absolute; left: 0; width: 722px; top: 274px; text-align: center; color: var(--white); font-size: 6.6px; }
  .social { position: absolute; left: 0; width: 722px; top: 289px; display: flex; justify-content: center; gap: 11px; }
  .social span { width: 8px; height: 8px; border-radius: 50%; background: var(--white); }
</style>
</head>
<body>

<header class="site-header">
  <div class="brand"><span class="brand-mark"></span><span class="brand-name">Velno Recycling</span></div>
  <nav class="main-nav">
    <a href="#" class="is-active">HOME</a>
    <a href="#">NEW PAGE</a>
    <a href="#">BOOK ONLINE</a>
  </nav>
</header>

<section class="hero">
  <h2 class="hero-kicker">COMPUTER RECYCLING</h2>
  <h1 class="hero-title">MADE <span>EASY</span></h1>
  <p class="hero-copy">Want to make a difference to our environment and planet? Velno Recycling is here to help! Velno recycling has been helping keep the environment healthy since 2006, we specialize in recycling services that help citizens become experts at reducing waste. We have a passion to keep our world clean and are here to guide you through all the stages of the recycling process.</p>
  <a href="#" class="btn">FIND OUT MORE</a>
  <div class="hero-media" role="img" aria-label="Photo of a blue recycling bin filled with old computer monitors, keyboards and cables"></div>
</section>

<section class="about">
  <div class="about-media" role="img" aria-label="Illustration of electronic devices falling into a green recycling bin"></div>
  <h2 class="section-title">ABOUT US</h2>
  <p class="about-copy">At Velno Recycling, we're committed to providing environmentally friendly recycling solutions to Austin and the surrounding areas. Founded in 2006, our mission is to process your materials in a safe, non-hazardous manner — with an aim to keep the world environmentally clean. As a R2 recycling center, we believe in promoting smart recycling habits in order to achieve long lasting results.</p>
  <a href="#" class="btn">SCHEDULE A PICKUP</a>
</section>

<section class="services">
  <h2 class="section-title">RECYCLING SERVICES</h2>

  <article class="service service--ewaste">
    <svg class="service-icon" viewBox="0 0 80 70" width="80" height="70" aria-hidden="true">
      <rect x="1" y="2" width="78" height="50" rx="3" fill="#595959"/>
      <rect x="5" y="6" width="70" height="42" fill="#fff"/>
      <rect x="34" y="52" width="12" height="10" fill="#595959"/>
      <rect x="24" y="62" width="32" height="5" rx="1" fill="#595959"/>
      <path d="M40 15 L49 30 H31 Z" fill="none" stroke="#595959" stroke-width="4" stroke-linejoin="round"/>
      <path d="M45 20 l5 -1 l-1 5" fill="none" stroke="#595959" stroke-width="2"/>
    </svg>
    <h3 class="service-name">Electronic Recycling</h3>
    <p class="service-tag">Environmentally Friendly</p>
    <p class="service-copy">At Velno Recycling, we strive to keep the environment clean through our wide range of services. Our E-Waste Recycling services were designed to simplify the recycling process for residents in the Austin area. Contact us today and see how you can contribute to making this world a cleaner place.</p>
  </article>

  <article class="service service--pickup">
    <svg class="service-icon" viewBox="0 0 70 72" width="66" height="70" aria-hidden="true">
      <g fill="#1273c4">
        <circle cx="20" cy="18" r="17"/>
        <rect x="2" y="38" width="36" height="22"/>
        <path d="M40 44 H56 L66 54 V60 H40 Z"/>
        <circle cx="14" cy="64" r="7"/>
        <circle cx="54" cy="64" r="7"/>
      </g>
      <circle cx="20" cy="18" r="12" fill="#fff"/>
      <path d="M20 10 V18 H27" fill="none" stroke="#1273c4" stroke-width="3"/>
      <circle cx="14" cy="64" r="3" fill="#fff"/>
      <circle cx="54" cy="64" r="3" fill="#fff"/>
      <rect x="45" y="47" width="9" height="6" fill="#fff"/>
    </svg>
    <h3 class="service-name">Recycling Pickup</h3>
    <p class="service-tag">We Come To You</p>
    <p class="service-copy">At Velno Recycling, we go out of our way to make sure your recycling process is made easy as possible. Our Recycling Pickup service is designed to simplify all of your recycling needs . Take a look at all the services we offer and get in touch to see how you can start the process today!</p>
  </article>
</section>

<section class="contact">
  <div class="contact-backdrop" role="img" aria-label="Blue-tinted photo of people working at laptops in an office"></div>
  <h2 class="contact-title">CONTACT US</h2>
  <form class="contact-form">
    <div class="field">Your Name</div>
    <div class="field">Your Email</div>
    <div class="field">Company Name</div>
    <div class="field field--message">Your Message</div>
    <div class="btn-submit">SUBMIT NOW</div>
  </form>
  <p class="contact-details">dana@velnorecycling.com &nbsp;-&nbsp; (512)555-0142 &nbsp;-&nbsp; 4120 Larkspur Lane Austin TX USA 78745</p>
  <p class="copyright">©2018 by Velno Recycling. All Right Reserved</p>
  <div class="social" aria-label="Social links"><span></span><span></span><span></span></div>
</section>

</body>
</html>
```